A new web site design for Volkanti.com

Create a new clean and modern design for Volkanti.com. This site will be a straight HTML site that will feature videos, PDF downloads, contact us page and marketing capture forms in front of some of the downloadable content. Brightpeak is an example of a related product and an example of what we consider a good design ( https://www.brightpeakhub.example/ ) We are open to any design and colours schemes however we have an existing logo. I have also attached a PDF brochure design that we had built before for reference, and a word document with the menu structure and some initial content.
Target Market(s)
CIO of large corporations
Industry/Entity Type
Saas

```html
<!DOCTYPE html>
<html lang="en">
<head>
<meta charset="utf-8">
<title>Volkanti — Technology Business Management</title>
<link href="https://fonts.googleapis.com/css2?family=Lato:wght@300;400;700;900&display=swap" rel="stylesheet">
<style>
:root{
  --blue:#00b4ef;
  --blue-dark:#0099d4;
  --ink:#2b2b33;
  --text:#7a7a82;
  --muted:#a4a4ab;
  --line:#e3e6ea;
  --night:#1d1f25;
  --night-2:#26282f;
  --white:#fff;
  --soft:#f4f5f7;
}
*{box-sizing:border-box;margin:0;padding:0}
html,body{width:1200px;height:4813px;overflow:hidden}
body{font-family:'Lato',Arial,sans-serif;color:var(--text);background:var(--white);font-size:13px;line-height:1.6}
section,header,footer{position:relative;width:1200px;overflow:hidden}
.center{text-align:center}
.section-title{font-size:27px;font-weight:300;color:var(--ink);text-align:center}
.section-title b{font-weight:900;color:var(--blue);text-transform:uppercase}
.section-sub{width:620px;margin:10px auto 0;text-align:center;font-size:12px;color:var(--muted)}

/* hero */
.hero{height:578px;background:radial-gradient(ellipse at 70% 55%,#4a5566 0%,#232a36 50%,#12151c 100%)}
.hero-photo{position:absolute;inset:0;background:linear-gradient(120deg,rgba(60,75,95,.5),rgba(20,24,32,.2) 60%,rgba(80,90,105,.35))}
.brand{position:absolute;left:45px;top:58px;display:flex;align-items:center;gap:8px;color:var(--white)}
.brand-dot{width:10px;height:10px;border-radius:50%;background:var(--white)}
.brand-name{font-size:19px;font-weight:400;line-height:1}
.nav{position:absolute;left:470px;top:62px;display:flex;gap:6px}
.nav a{color:var(--white);text-decoration:none;font-size:12px;padding:5px 13px;border-radius:14px}
.nav a.active{border:1px solid var(--blue)}
.topbar{position:absolute;right:45px;top:18px;display:flex;align-items:center;gap:8px;color:var(--white);font-size:11px}
.flag{width:18px;height:12px;background:linear-gradient(#c8102e 50%,#fff 50%)}
.dot-social{width:16px;height:16px;border-radius:50%;background:var(--blue)}
.hero-lead{position:absolute;top:226px;width:100%;text-align:center;color:var(--white);font-size:20px;font-weight:300}
.hero-title{position:absolute;top:260px;width:100%;text-align:center;color:var(--blue);font-size:34px;font-weight:900;letter-spacing:.3px}
.btn-ghost{position:absolute;left:510px;top:354px;width:180px;height:44px;border:2px solid var(--white);border-radius:22px;color:var(--white);font-size:11px;font-weight:700;display:flex;align-items:center;justify-content:center;letter-spacing:.5px}
.slide-arrow{position:absolute;top:320px;width:36px;height:36px;border-radius:50%;background:rgba(0,0,0,.55)}

/* intro */
.intro{height:658px}
.intro .section-title{position:absolute;top:78px;width:100%}
.intro .section-sub{position:absolute;top:124px;left:290px;margin:0}
.phone-art{position:absolute;left:145px;top:208px;width:288px;height:290px;border-radius:18px;background:linear-gradient(135deg,#3a3f48,#15181d 60%,#c9ccd1)}
.intro-copy{position:absolute;left:472px;top:232px;width:590px}
.intro-copy h3{font-size:19px;font-weight:700;color:var(--ink);margin-bottom:10px}
.intro-copy p{font-size:12px;color:var(--muted)}
.ticks{list-style:none;margin-top:14px}
.ticks li{font-size:12px;color:var(--muted);display:flex;align-items:center;gap:8px;margin-bottom:8px}
.ticks b{color:var(--ink)}
.tick{width:11px;height:11px;border-radius:50%;background:var(--blue)}
.btn-row{display:flex;gap:14px;margin-top:22px}
.btn{width:100px;height:34px;border-radius:17px;font-size:10px;font-weight:700;display:flex;align-items:center;justify-content:center}
.btn-solid{background:var(--blue);color:var(--white)}
.btn-line{border:1px solid var(--line);color:var(--muted)}

/* blue band */
.band{height:417px;background:var(--blue);color:var(--white)}
.band h2{position:absolute;left:145px;top:84px;font-size:23px;font-weight:300}
.band h2 b{font-weight:900;text-transform:uppercase}
.band-copy{position:absolute;left:145px;top:132px;width:590px;font-size:12px;line-height:1.7}
.band-copy p+p{margin-top:10px}
.checks{position:absolute;left:145px;top:300px;display:grid;grid-template-columns:180px 180px;gap:10px 6px;font-size:11px}
.checks span{display:flex;align-items:center;gap:8px}
.box{width:12px;height:12px;border:1px solid var(--white)}
.person-art{position:absolute;left:855px;top:0;width:210px;height:417px;background:linear-gradient(180deg,#3a2b24,#5d7ea8 45%,#9fb8d8)}

/* features */
.features{height:909px}
.features .section-title{position:absolute;top:110px;width:100%}
.features .section-sub{position:absolute;top:152px;left:290px;margin:0}
.orbit{position:absolute;left:0;top:0}
.device-art{position:absolute;left:455px;top:265px;width:380px;height:330px;border-radius:30px;background:linear-gradient(150deg,#eceef1,#2a2f45 30%,#1c2033 70%,#e6e8ec)}
.feature{position:absolute;width:190px}
.feature h4{font-size:15px;color:var(--ink);font-weight:700;margin:8px 0 4px}
.feature p{font-size:10px;color:var(--muted);line-height:1.5}
.f-icon{width:46px;height:46px;border-radius:50%;border:1px solid var(--line);background:var(--white);display:flex;align-items:center;justify-content:center}

/* video */
.video{height:408px;background:linear-gradient(180deg,#3d3a33,#5a5647 40%,#2a2924)}
.video h2{position:absolute;top:162px;width:100%;text-align:center;color:var(--white);font-size:28px;font-weight:300}
.video h2 b{color:var(--blue);font-weight:900;text-transform:uppercase}
.video p{position:absolute;top:205px;width:100%;text-align:center;color:var(--white);font-size:12px}
.play{position:absolute;left:580px;top:250px}

/* testimonials */
.testimonials{height:505px}
.testimonials .section-title{position:absolute;top:70px;width:100%}
.testimonials .section-sub{position:absolute;top:110px;left:290px;margin:0}
.quote-card{position:absolute;top:224px;width:450px;height:202px;background:var(--white);box-shadow:0 2px 10px rgba(0,0,0,.1);display:flex}
.quote-photo{width:180px;height:202px;flex:none;background:linear-gradient(135deg,#cfc4b6,#8c7a68);clip-path:polygon(0 0,100% 0,72% 100%,0 100%)}
.quote-body{padding:34px 20px 0 4px;font-size:11px;color:var(--muted)}
.quote-mark{color:var(--blue);font-size:40px;font-weight:900;line-height:.7}
.quote-name{margin-top:18px;font-size:10px;font-weight:900;color:var(--ink)}
.dots{position:absolute;top:475px;left:586px;display:flex;gap:6px}
.dots i{width:6px;height:6px;border-radius:50%;background:#ccc}
.dots i:first-child{background:var(--blue)}

/* partners */
.partners{height:138px;background:var(--blue);display:flex;align-items:center;justify-content:center;gap:62px;color:var(--white);font-size:16px;font-weight:700}

/* posts */
.posts{height:700px}
.posts .section-title{position:absolute;top:70px;width:100%;font-weight:400;font-size:23px}
.posts .section-sub{position:absolute;top:108px;left:290px;margin:0}
.post{position:absolute;top:190px;width:290px;height:428px;background:var(--soft)}
.post-img{height:198px}
.post-body{padding:24px 20px}
.post h3{font-size:15px;font-weight:900;color:var(--ink);line-height:1.3}
.post time{display:block;font-size:10px;color:var(--muted);margin:6px 0 10px}
.post p{font-size:11px;color:var(--muted)}
.read{margin-top:20px;font-size:11px;font-weight:900;color:var(--ink)}

/* footer */
.footer{height:502px;background:linear-gradient(180deg,var(--night-2),var(--night))}
.contact-card{position:absolute;left:148px;top:70px;width:262px;height:372px;background:var(--white);padding:26px 22px;font-size:11px}
.contact-card h5{color:var(--blue);font-size:11px;font-weight:900;margin-bottom:6px}
.contact-card .line{display:flex;align-items:center;gap:6px;color:var(--blue);font-weight:900;font-size:10px;margin-top:16px}
.contact-card p{color:var(--muted)}
.map-art{position:absolute;left:410px;top:70px;width:335px;height:372px;background:linear-gradient(135deg,#eef0ec,#dfe4dc)}
.comment-box{position:absolute;left:745px;top:70px;width:308px;height:372px;background:#121317;padding:24px 22px}
.comment-box h5{color:var(--white);font-size:12px;font-weight:900;margin-bottom:24px}
.field{height:30px;border:1px solid #3a3c44;margin-bottom:12px;color:#666;font-size:10px;padding:8px 10px}
.field.tall{height:96px}
.submit{width:90px;height:30px;border-radius:15px;background:var(--blue);color:var(--white);font-size:10px;font-weight:900;display:flex;align-items:center;justify-content:center;margin-left:auto;margin-right:auto}
.copyright{position:absolute;top:478px;width:100%;text-align:center;font-size:10px;color:#8a8c93}
</style>
</head>
<body>

<header class="hero">
  <div class="hero-photo" role="img" aria-label="Hand touching a screen with cloud and network icons"></div>
  <div class="brand"><span class="brand-dot"></span><span class="brand-name">Volkanti</span></div>
  <div class="topbar"><span class="flag"></span><span>English ▾</span><span class="dot-social"></span><span class="dot-social"></span><span class="dot-social"></span></div>
  <nav class="nav"><a class="active">Home</a><a>Model Example</a><a>Pricing</a><a>Resources</a><a>Consultancies</a><a>About Us</a><a>Contact</a></nav>
  <div class="hero-lead">Show the value delivered by IT to the business using</div>
  <h1 class="hero-title">TECHNOLOGY BUSINESS MANAGEMENT</h1>
  <div class="btn-ghost">WATCH THE VIDEO</div>
  <div class="slide-arrow" style="left:98px"><svg width="36" height="36"><path d="M20 12l-6 6 6 6" stroke="#fff" stroke-width="2" fill="none"/></svg></div>
  <div class="slide-arrow" style="left:1066px"><svg width="36" height="36"><path d="M16 12l6 6-6 6" stroke="#fff" stroke-width="2" fill="none"/></svg></div>
</header>

<section class="intro">
  <h2 class="section-title">Maecenas interdum metus <b>id euismod dapibus</b></h2>
  <p class="section-sub">Nullam ut lorem tincidunt euismod volutpat porta nisi. Maecenas pellentesque facilisi augue nec scelerisque et commodo. Sed ut lacus est fermentum dictum sagittis pharetra. Fusce blandit id diam nec luctus egestas tincidunt.</p>
  <div class="phone-art" role="img" aria-label="Two smartphones showing the app menu"></div>
  <div class="intro-copy">
    <h3>Quisque bibendum sem a euismod sagittis</h3>
    <p>Nullam ut tortor dictum, lobortis urna in, aliquam arcu. Vivamus id congue mi elit. Nam porta dui at pulvinar faucibus. Phasellus ut luctus ultricies faucibus quam ut rhoncus nulla. Sed vestibulum lorem diam. Donec hendrerit in nibh ac maximus velit pellentesque at. Phasellus in interdum lacus. Etiam feugiat neque a nisl laoreet tempor. Sed vestibulum lorem diam. Donec hendrerit in nibh ac maximus velit pellentesque at. Phasellus in interdum lacus.</p>
    <ul class="ticks">
      <li><span class="tick"></span><span><b>Vestibulum</b> eget ultrices vel nullam</span></li>
      <li><span class="tick"></span><span><b>Mattis</b> vulputate venenatis quisque</span></li>
      <li><span class="tick"></span><span><b>Egeluctt</b> lorem feugiat tincidunt ornare</span></li>
      <li><span class="tick"></span><span><b>Consequat</b> vitae sem ut lacus mollis</span></li>
    </ul>
    <div class="btn-row"><span class="btn btn-solid">SEE MORE</span><span class="btn btn-line">DOWNLOAD</span></div>
  </div>
</section>

<section class="band">
  <h2>Praesent mattis vestibulum iaculis <b>nullam tincidunt</b></h2>
  <div class="band-copy">
    <p>Ut euismod elementum, suspendisse potenti. Ut ultrices quam nec suscipit tincidunt, nunc pellentesque lacus faucibus, quam ut lorem dolor rhoncus nisl. Nam mauris purus nec tristique tellus. Donec pharetra dui ut scelerisque dictum ipsum neque ornare diam.</p>
    <p>Ut sed ultrices et creas at tortor. Morbi mattis libero nec justo ullamcorper faucibus. Donec nec dolor et dolor molestie convallis ut sit amet nisi. Morbi faucibus phasellus erat ut porta nunc sed. Nullam non dictum arcu. Cras sit amet nunc sed magna tempus vestibulum lorem.</p>
  </div>
  <div class="checks">
    <span><i class="box"></i>Donec felis nulla vestibulum</span><span><i class="box"></i>Donec felis nulla vestibulum</span>
    <span><i class="box"></i>Donec felis nulla vestibulum</span><span><i class="box"></i>Donec felis nulla vestibulum</span>
  </div>
  <div class="person-art" role="img" aria-label="Smiling man in a denim shirt holding a phone"></div>
</section>

<section class="features">
  <h2 class="section-title">Suspendisse potenti ultrices quam nec <b>suspicit tincidunt</b></h2>
  <p class="section-sub">Nunc dui dui sapien, faucibus posuere sapien lacus metus erat. Nunc et lacus purus nec sollicitudin tristique netus. Donec pharetra, lacus nec scelerisque ipsum, ipsum mauris dictum dolor sit amet dictum ut commodo vitae nisl.</p>
  <svg class="orbit" width="1200" height="909">
    <circle cx="640" cy="440" r="330" fill="none" stroke="#e6e9ed" stroke-width="1.5"/>
    <path d="M250 380 Q380 250 560 300" fill="none" stroke="#e6e9ed" stroke-width="1.5"/>
    <path d="M700 620 Q820 760 960 640" fill="none" stroke="#e6e9ed" stroke-width="1.5"/>
  </svg>
  <div class="device-art" role="img" aria-label="Smartphone lying flat showing a dark app screen"></div>

  <div class="feature center" style="left:185px;top:310px">
    <div class="f-icon" style="margin:0 auto"><svg width="20" height="20"><path d="M5 4l3-2h4l3 2 3 3-3 2v9H5V9L2 7z" fill="none" stroke="#00b4ef" stroke-width="1.5"/></svg></div>
    <h4>Donec Pulvinar</h4><p>Vulputate erat non elementum. Aenean maximus pharetra varius. Morbi vehicula risus eget velit faucibus, nec maximus sapien fermentum.</p>
  </div>
  <div class="feature center" style="left:825px;top:218px">
    <div class="f-icon" style="margin:0 auto"><svg width="20" height="20"><path d="M4 7l3-4h6l3 4-6 10z M4 7h12" fill="none" stroke="#00b4ef" stroke-width="1.5"/></svg></div>
    <h4>Donec Pulvinar</h4><p>Vulputate erat non elementum. Aenean maximus pharetra varius. Morbi vehicula risus eget velit faucibus, nec maximus sapien fermentum.</p>
  </div>
  <div class="feature center" style="left:825px;top:530px">
    <div class="f-icon" style="margin:0 auto"><svg width="20" height="20"><path d="M3 7h13l-3-3M17 13H4l3 3" fill="none" stroke="#00b4ef" stroke-width="1.5"/></svg></div>
    <h4>Donec Pulvinar</h4><p>Vulputate erat non elementum. Aenean maximus pharetra varius. Morbi vehicula risus eget velit faucibus, nec maximus sapien fermentum.</p>
  </div>
  <div class="feature center" style="left:245px;top:600px">
    <div class="f-icon" style="margin:0 auto"><svg width="20" height="20"><path d="M10 2C7 7 5 10 5 13a5 5 0 0010 0c0-3-2-6-5-11z" fill="none" stroke="#00b4ef" stroke-width="1.5"/></svg></div>
    <h4>Donec Pulvinar</h4><p>Vulputate erat non elementum. Aenean maximus pharetra varius. Morbi vehicula risus eget velit faucibus, nec maximus sapien fermentum.</p>
  </div>
</section>

<section class="video" role="img" aria-label="Misty landscape with a rope bridge between rock pillars">
  <h2>Quick Video <b>demonstration</b></h2>
  <p>Morbi mattis libero nec justo ullamcorper faucibus. Donec nec dolor et dolor molestie convallis ut sit amet erat. Morbi faucibus pharetra erat.</p>
  <svg class="play" width="40" height="40"><circle cx="20" cy="20" r="18" fill="none" stroke="#00b4ef" stroke-width="2"/><path d="M16 13l10 7-10 7z" fill="#00b4ef"/></svg>
</section>

<section class="testimonials">
  <h2 class="section-title">What people are <b>saying</b></h2>
  <p class="section-sub">Donec felis tortor, vestibulum volutpat tellus at, ornare rutrum elementum ex. Quisque bibendum sem a euismod sagittis. Nullam at tortor dictum, lobortis urna in, aliquam arcu.</p>
  <div class="quote-card" style="left:148px">
    <div class="quote-photo" role="img" aria-label="Portrait of a smiling client"></div>
    <div class="quote-body"><div class="quote-mark">“</div><p>Praesent mattis vestibulum iaculis. Nullam tincidunt congue ut consectetur dolor suscipit.</p><div class="quote-name">SUSPENDISSE POTENTI</div></div>
  </div>
  <div class="quote-card" style="left:603px">
    <div class="quote-photo" role="img" aria-label="Portrait of a smiling client with glasses"></div>
    <div class="quote-body"><div class="quote-mark">“</div><p>Praesent mattis vestibulum iaculis. Nullam tincidunt congue ut consectetur dolor suscipit.</p><div class="quote-name">SUSPENDISSE POTENTI</div></div>
  </div>
  <div class="dots"><i></i><i></i><i></i></div>
</section>

<section class="partners">
  <span>Harlow Firm</span><span>Castellan</span><span>Skyvane</span><span>Arcnode</span><span>Eastbrook</span><span>Globeline</span>
</section>

<section class="posts">
  <h2 class="section-title">LATEST POSTS</h2>
  <p class="section-sub">Donec felis tortor, vestibulum volutpat tellus at, ornare rutrum elementum ex. Quisque bibendum sem a euismod sagittis. Nullam at tortor dictum, lobortis urna in, aliquam arcu.</p>
  <article class="post" style="left:148px">
    <div class="post-img" role="img" aria-label="Man working on a laptop" style="background:linear-gradient(135deg,#d9d3c8,#8d8376)"></div>
    <div class="post-body"><h3>PRAESENT MATTIS VESTIBULUM IACULIS NULLAM TINCIDUNT</h3><time>March 21, 2017</time><p>Sed a lacus congue, et accumsan diam pharetra. Suspendisse potenti. Ut ultrices, quam nec suscipit tincidunt, nunc dui feugiat lacus.</p><div class="read">READ MORE →</div></div>
  </article>
  <article class="post" style="left:456px">
    <div class="post-img" role="img" aria-label="Woman smiling at her phone" style="background:linear-gradient(135deg,#e3d39a,#9a8450)"></div>
    <div class="post-body"><h3>PRAESENT MATTIS VESTIBULUM IACULIS NULLAM TINCIDUNT</h3><time>March 21, 2017</time><p>Sed a lacus congue, et accumsan diam pharetra. Suspendisse potenti. Ut ultrices, quam nec suscipit tincidunt, nunc dui feugiat lacus.</p><div class="read">READ MORE →</div></div>
  </article>
  <article class="post" style="left:764px">
    <div class="post-img" role="img" aria-label="Hand holding a phone at sunset" style="background:linear-gradient(135deg,#f2b266,#6b4a38)"></div>
    <div class="post-body"><h3>PRAESENT MATTIS VESTIBULUM IACULIS NULLAM TINCIDUNT</h3><time>March 21, 2017</time><p>Sed a lacus congue, et accumsan diam pharetra. Suspendisse potenti. Ut ultrices, quam nec suscipit tincidunt, nunc dui feugiat lacus.</p><div class="read">READ MORE →</div></div>
  </article>
</section>

<footer class="footer">
  <div class="contact-card">
    <h5>CONTACT US</h5>
    <p>Donec interdum dapibus lacinia aliquam congue tempus augue nec elementum iaculis dui.</p>
    <div class="line"><svg width="10" height="12"><path d="M5 11C2 7 1 5.5 1 4a4 4 0 018 0c0 1.5-1 3-4 7z" fill="#00b4ef"/></svg>LOCATION</div>
    <p>372, Donec Sed, Nullam At</p>
    <div class="line"><svg width="10" height="12"><path d="M2 1h2l1 3-1 1a6 6 0 003 3l1-1 3 1v2a1 1 0 01-1 1C5 11 1 7 1 2a1 1 0 011-1z" fill="#00b4ef"/></svg>PHONE</div>
    <p>(+1) 555-019-2047</p>
    <div class="line"><svg width="12" height="10"><rect x=".5" y=".5" width="11" height="9" fill="none" stroke="#00b4ef"/><path d="M1 1l5 4 5-4" fill="none" stroke="#00b4ef"/></svg>E-MAIL</div>
    <p>hello@volkanti.com</p>
  </div>
  <div class="map-art" role="img" aria-label="Street map with a location pin"></div>
  <div class="comment-box">
    <h5>LEAVE A COMMENT</h5>
    <div class="field">Your Name</div>
    <div class="field">Your Email</div>
    <div class="field tall">Message</div>
    <div class="submit">SUBMIT</div>
  </div>
  <div class="copyright">Copyright © Volkanti.com 2017. All rights reserved.</div>
</footer>

</body>
</html>
```